New Menu for Elegant Cafe Pastry Shop

We need to choose a design and layout for our new menu. We would like to also condense our current menu to 4-6 pages.
We will be changing prices and items on the menu, so it needs to be editable. Adobe formats are preferred. The size of the pages needs to be letter size. We will be printing it in house
Please take inspiration from the photos of our shop and food and also our Instagram page.
Attached are our current menu our logo and the logo info

https://www.snapgrid.example/brioweldon/?hl=en
https://maps.example-locate.net/qT7mWx2KpLr9vBn4C

Industry/Entity Type

Food Cafe Bakery pastry

Font styles to use
Other font styles liked:
• please look at attached files

Colors

Designer to choose colors to be used in the design.

Requirements
Nice to have
• Use of Arches like on our shop wallpaper or oblong eclair shapes, Art Deco elements

```html
<!DOCTYPE html>
<html lang="en">
<head>
<meta charset="utf-8">
<title>Brioweldon — New Menu</title>
<link href="https://fonts.googleapis.com/css2?family=Italiana&family=Cinzel:wght@600&family=Tinos&display=swap" rel="stylesheet">
<style>
:root{
  --board:#58524f;
  --paper:#ffffff;
  --teal:#4cc2c8;
  --plum:#3b1a2d;
  --ink:#2a1a22;
  --photo-warm:#c98a4b;
  --photo-cool:#cfe3e6;
}
*{margin:0;padding:0;box-sizing:border-box}
html,body{width:668px;height:1200px;overflow:hidden;background:var(--board)}
.board{position:relative;width:668px;height:1200px}
.page{position:absolute;width:270px;height:348px;background:var(--paper);overflow:hidden;color:var(--ink)}
.p1{left:50px;top:40px}.p2{left:339px;top:40px}
.p3{left:50px;top:410px}.p4{left:339px;top:410px}
.p5{left:50px;top:780px}.p6{left:339px;top:780px}
.frame{position:absolute;inset:7px;border:.8px solid var(--teal);pointer-events:none}
.corner{position:absolute;width:16px;height:16px;background:var(--plum);border-radius:50% 10% 50% 10%;opacity:.9}
.c-tl{left:3px;top:3px}.c-tr{right:3px;top:3px;transform:scaleX(-1)}
.c-bl{left:3px;bottom:3px;transform:scaleY(-1)}.c-br{right:3px;bottom:3px;transform:scale(-1,-1)}
.col{position:absolute;width:112px}
.col.l{left:20px}.col.r{left:138px}
.big{font-family:"Italiana",serif;color:var(--plum);font-size:17px;line-height:1}
.sub{font-family:"Tinos",serif;font-size:4px;color:var(--plum)}
.hd{font-family:"Italiana",serif;font-size:8.5px;color:var(--plum);display:flex;align-items:center;gap:3px;margin:6px 0 2.5px;white-space:nowrap}
.hd::after{content:"";flex:1;height:4px;background:radial-gradient(circle at right center,var(--teal) 1.6px,transparent 1.9px),linear-gradient(var(--teal),var(--teal)) left center/calc(100% - 4px) .9px no-repeat}
.row{display:flex;align-items:flex-end;font-family:"Tinos",serif;font-size:3.2px;line-height:1.55;text-transform:uppercase}
.row .ld{flex:1;border-bottom:.35px dotted var(--ink);margin:0 1px 1px}
.dish{font-family:"Italiana",serif;font-size:5.6px;color:var(--plum);margin-top:3px}
.desc{font-family:"Tinos",serif;font-size:3.1px;line-height:1.5;display:flex;align-items:flex-end}
.desc .t{max-width:72%}
.desc .ld{flex:1;border-bottom:.35px dotted var(--ink);margin:0 1px 1px}
.photo{position:absolute}
/* cover */
.cover-photo{inset:0;background:linear-gradient(135deg,var(--photo-cool) 0%,#e8c3a6 30%,var(--photo-warm) 60%,#8c6a3a 100%)}
.badge{position:absolute;left:24px;top:40px;width:222px;height:270px;background:var(--plum);border-radius:50%/42%}
.badge-inner{position:absolute;left:8px;top:8px;right:8px;bottom:8px;background:var(--paper);border-radius:50%/42%;text-align:center}
.brand{font-family:"Cinzel",serif;font-weight:600;font-size:17px;color:var(--plum);margin-top:120px;letter-spacing:.5px}
.new{font-family:"Tinos",serif;font-size:12px;color:var(--plum);margin-top:38px}
.hours{font-family:"Tinos",serif;font-size:3.4px;line-height:1.5;color:var(--plum);margin-top:4px}
.emblem{position:absolute;left:80px;top:40px;width:46px;height:60px;border:2px solid var(--teal);border-radius:50% 50% 12px 12px}
.legend{position:absolute;font-family:"Tinos",serif;font-size:3.1px;line-height:1.5;color:var(--plum)}
.note{position:absolute;left:12px;top:237px;background:var(--plum);color:#fff;font-family:"Tinos",serif;font-size:2.9px;padding:1.5px 3px;width:54px}
</style>
</head>
<body>
<div class="board">

<!-- Cover -->
<section class="page p1">
  <div class="photo cover-photo" role="img" aria-label="Photo of pastries, cheesecake, savory eclairs and salad on a table"></div>
  <div class="badge">
    <div class="badge-inner">
      <div class="emblem" role="img" aria-label="Arched emblem area"></div>
      <div class="brand">BRIOWELDON</div>
      <div class="new">NEW MENU</div>
      <div class="hours">SUNDAY - WEDNESDAY<br>9 AM – 6 PM<br>THURSDAY - SATURDAY<br>9 AM – 7 PM</div>
    </div>
  </div>
</section>

<!-- Drinks & seasonal -->
<section class="page p2">
  <div class="frame"></div>
  <div class="corner c-tl" role="img" aria-label="Corner ornament"></div><div class="corner c-tr" role="img" aria-label="Corner ornament"></div>
  <div class="corner c-bl" role="img" aria-label="Corner ornament"></div><div class="corner c-br" role="img" aria-label="Corner ornament"></div>
  <div class="col l" style="top:18px">
    <div class="big" style="font-size:16px">Seasonal</div>
    <div class="sub" style="margin-left:32px">Upon Availability</div>
    <div class="hd">Soups</div>
    <div class="row"><span>Lorraine</span><span class="ld"></span><span>$0.00</span></div>
    <div class="hd">Travel Cakes V</div>
    <div class="row"><span>Banana Pecan (CN)</span><span class="ld"></span><span>$0.00</span></div>
    <div class="row"><span>Banana Walnut (CN)</span><span class="ld"></span><span>$0.00</span></div>
    <div class="row"><span>Banana Chocolate Chips</span><span class="ld"></span><span>$0.00</span></div>
    <div class="row"><span>Blueberry</span><span class="ld"></span><span>$0.00</span></div>
    <div class="row"><span>Pistachio Raspberry Opera (CN)</span><span class="ld"></span><span>$0.00</span></div>
    <div class="desc"><span class="t">Pistachio joconde cake layered with pistachio buttercream, chocolate ganache and raspberry gelée.</span></div>
    <div class="hd">Baba Au Rhum</div>
    <div class="desc"><span class="t">Chocolate / Nocciola</span><span class="ld"></span>$0.00</div>
    <div class="desc"><span class="t">vanilla/orange/pineapple</span><span class="ld"></span>$0.00</div>
    <div class="big" style="margin-top:5px">Mocktails</div>
    <div class="hd">Pina Colada</div>
    <div class="desc"><span class="t">A tropical classic mocktail of pineapple and coconut</span><span class="ld"></span>$0.00</div>
    <div class="hd">Mango Lychee</div>
    <div class="desc"><span class="t">Refreshing mix of lychee and mango</span><span class="ld"></span>$0.00</div>
    <div class="hd">Shirley Temple</div>
    <div class="desc"><span class="t">Ginger ale and grenadine mocktail garnished with maraschino cherry.</span><span class="ld"></span>$0.00</div>
    <div class="big" style="margin-top:6px;line-height:.95">Coffees &amp;<br>Beverages</div>
    <div class="hd">Iced Coffee</div>
    <div class="row"><span>Iced Espresso</span><span class="ld"></span><span>$0.00</span></div>
    <div class="row"><span>Iced Cappuccino</span><span class="ld"></span><span>$0.00</span></div>
    <div class="row"><span>Iced Latte</span><span class="ld"></span><span>$0.00</span></div>
  </div>
  <div class="col r" style="top:20px">
    <div class="hd">Hot Coffee</div>
    <div class="row"><span>Filter Coffee</span><span class="ld"></span><span>$0.00</span></div>
    <div class="row"><span>Espresso</span><span class="ld"></span><span>$0.00</span></div>
    <div class="row"><span>Cappuccino</span><span class="ld"></span><span>$0.00</span></div>
    <div class="row"><span>Latte</span><span class="ld"></span><span>$0.00</span></div>
    <div class="row"><span>Americano</span><span class="ld"></span><span>$0.00</span></div>
    <div class="row"><span>Espresso</span><span class="ld"></span><span>$0.00</span></div>
    <div class="row"><span>Macchiato</span><span class="ld"></span><span>$0.00</span></div>
    <div class="hd">Matcha</div>
    <div class="row"><span>Matcha Tea</span><span class="ld"></span><span>$0.00</span></div>
    <div class="row"><span>Matcha</span><span class="ld"></span><span>$0.00</span></div>
    <div class="row"><span>Latte Hot</span><span class="ld"></span><span>$0.00</span></div>
    <div class="row"><span>Matcha</span><span class="ld"></span><span>$0.00</span></div>
    <div class="row"><span>Latte Cold</span><span class="ld"></span><span>$0.00</span></div>
    <div class="hd">Syrups - Sauces - Toppings</div>
    <div class="desc"><span class="t">Vanilla | Hazelnut | caramel | mocha | lavender | almond</span></div>
    <div class="desc"><span class="t">(ask for our sugar free options)+</span><span class="ld"></span>$0.00</div>
    <div class="desc"><span class="t">dark or white chocolate sauce +</span><span class="ld"></span>$0.00</div>
    <div class="desc"><span class="t">extra shot +</span><span class="ld"></span>$0.00</div>
    <div class="desc"><span class="t">Decaf +</span><span class="ld"></span>$0.00</div>
    <div class="hd">Cold Drinks</div>
    <div class="row"><span>Isla Water 16 oz</span><span class="ld"></span><span>$0.00</span></div>
    <div class="row"><span>San Fontello</span><span class="ld"></span><span>$0.00</span></div>
    <div class="row"><span>Cola Classica / Diet</span><span class="ld"></span><span>$0.00</span></div>
    <div class="row"><span>Perlette</span><span class="ld"></span><span>$0.00</span></div>
    <div class="row"><span>Homemade Lemonade</span><span class="ld"></span><span>$0.00</span></div>
    <div class="row"><span>Mint Lemonade</span><span class="ld"></span><span>$0.00</span></div>
    <div class="row"><span>Strawberry Lemonade</span><span class="ld"></span><span>$0.00</span></div>
    <div class="row"><span>Lavender Lemonade</span><span class="ld"></span><span>$0.00</span></div>
    <div class="row"><span>Orange Juice</span><span class="ld"></span><span>$0.00</span></div>
    <div class="hd">Tea</div>
    <div class="row"><span>Earl Grey</span><span class="ld"></span><span>$0.00</span></div>
    <div class="row"><span>Darjeeling</span><span class="ld"></span><span>$0.00</span></div>
    <div class="row"><span>Ginger Lemongrass</span><span class="ld"></span><span>$0.00</span></div>
    <div class="row"><span>Camomile</span><span class="ld"></span><span>$0.00</span></div>
    <div class="row"><span>Mint Vervain &amp; Herbs</span><span class="ld"></span><span>$0.00</span></div>
    <div class="row"><span>Fruit Symphony</span><span class="ld"></span><span>$0.00</span></div>
    <div class="row"><span>Dragon Sencha Green Tea</span><span class="ld"></span><span>$0.00</span></div>
    <div class="row"><span>Iced Tea</span><span class="ld"></span><span>$0.00</span></div>
    <div class="hd">Chocolate</div>
    <div class="row"><span>Chocolate Hot</span><span class="ld"></span><span>$0.00</span></div>
    <div class="row"><span>Chocolate Cold</span><span class="ld"></span><span>$0.00</span></div>
    <div class="row"><span>Whipped Cream</span><span class="ld"></span><span>$0.00</span></div>
  </div>
</section>

<!-- All day brunch -->
<section class="page p3">
  <div class="photo" style="left:4px;right:4px;top:226px;bottom:0;background:linear-gradient(160deg,#f4efe8 0%,#f2d27a 40%,#c87a4a 75%,#8a4a2a 100%);opacity:.9" role="img" aria-label="Photo of a fried egg and bacon on a chou bun"></div>
  <div class="frame"></div>
  <div class="corner c-tl" role="img" aria-label="Corner ornament"></div><div class="corner c-tr" role="img" aria-label="Corner ornament"></div>
  <div class="corner c-bl" role="img" aria-label="Corner ornament"></div><div class="corner c-br" role="img" aria-label="Corner ornament"></div>
  <div class="big" style="position:absolute;left:72px;top:20px">All Day Brunch</div>
  <div class="sub" style="position:absolute;left:153px;top:37px;font-size:5px">Unique Flavors</div>
  <div class="col l" style="top:62px;width:110px">
    <div class="hd" style="margin-top:0">Grilled Cheese Sandwich</div>
    <div class="desc"><span class="t">Big chou bun 2 slices of fontina cheese, ham and bacon - the ultimate grilled cheese sandwich “a la eclair”</span><span class="ld"></span>$0.00</div>
    <div class="hd">Croque Monsieur</div>
    <div class="desc"><span class="t">Big chou bun served not filled with creamy bechamel sauce, gruyere cheese, ham and bacon</span><span class="ld"></span>$0.00</div>
    <div class="hd">Croque Madame</div>
    <div class="desc"><span class="t">Big chou bun served hot filled with creamy bechamel sauce, gruyere cheese, ham and bacon and topped with an egg sunny side up</span><span class="ld"></span>$0.00</div>
    <div class="hd" style="margin-top:9px">Eggcellent Choices</div>
    <div class="desc"><span class="t">Also available: Gluten Free Bun</span></div>
    <div class="dish">Eggs Florentine</div>
    <div class="desc"><span class="t">Chou bun topped with chieve cream cheese, saute spinach, 2 eggs and pink hollandaise sauce</span><span class="ld"></span>$0.00</div>
    <div class="dish">Eggs Benedict</div>
    <div class="desc"><span class="t">Chou bun topped whipped chive cream cheese, ham, 3 eggs, and pink hallandaise sauce</span><span class="ld"></span>$0.00</div>
    <div class="dish">Advocado &amp; Eggs</div>
    <div class="desc"><span class="t">Chou bun topped with chunky avocado smash, crumbled feta, 2 eggs, topped with spicy honey, oil, chili flackes and seasame</span><span class="ld"></span>$0.00</div>
    <div class="dish">Eggs Royal</div>
    <div class="desc"><span class="t">Chou bun, topped with whipped cream cheese with chise, smoked salmon, diced red onion, 2 eggs, pink hollandaise sauce, sesame seeds</span><span class="ld"></span>$0.00</div>
  </div>
  <div class="col" style="left:138px;top:62px;width:113px">
    <div class="hd" style="margin-top:0">Pancakes</div>
    <div class="dish">O.M.G. Eggs $ Bacon</div>
    <div class="desc"><span class="t">4 pancakes topped with grated gruyere, bacon, an egg sunny side up and served with a side of maple syrup</span><span class="ld"></span>$0.00</div>
    <div class="dish">Classic Nocciola &amp; Berries</div>
    <div class="desc"><span class="t">4 pancakes topped with Nocciola, fresh berries and whipped cream</span><span class="ld"></span>$0.00</div>
    <div class="dish">Tropical Guava &amp; Cheese</div>
    <div class="desc"><span class="t">4 pancakes topped with guava cream, cream cheese frosting, fresh raspberries and raspberry syrup</span><span class="ld"></span>$0.00</div>
    <div class="dish">Oriental (CN)</div>
    <div class="desc"><span class="t">4 pancakes topped with Orange cream, caramelized pistachios, crunchy phyllo and drizzled with honey cinnamon syrup</span><span class="ld"></span>$0.00</div>
    <div class="hd" style="margin-top:8px">Sides</div>
    <div class="row"><span>Eggs(1)</span><span class="ld"></span><span>$0.00</span></div>
    <div class="row"><span>Bacon (4 slices)</span><span class="ld"></span><span>$0.00</span></div>
    <div class="row"><span>Salmon</span><span class="ld"></span><span>$0.00</span></div>
    <div class="row"><span>Pancakes (2)</span><span class="ld"></span><span>$0.00</span></div>
    <div class="row"><span>Avocado Smash</span><span class="ld"></span><span>$0.00</span></div>
    <div class="row"><span>Fruit Bowl</span><span class="ld"></span><span>$0.00</span></div>
    <div class="row"><span>Green Salad</span><span class="ld"></span><span>$0.00</span></div>
  </div>
</section>

<!-- Lunch & savory -->
<section class="page p4">
  <div class="frame"></div>
  <div class="corner c-tl" role="img" aria-label="Corner ornament"></div><div class="corner c-tr" role="img" aria-label="Corner ornament"></div>
  <div class="corner c-bl" role="img" aria-label="Corner ornament"></div><div class="corner c-br" role="img" aria-label="Corner ornament"></div>
  <div class="col l" style="top:28px">
    <div class="big">Lunch</div>
    <div class="hd" style="margin-top:12px">Salads</div>
    <div class="dish">Greek</div>
    <div class="desc"><span class="t">Baby tomatoes, cucumbers, feta, olives, onions, P.O.V. olive oil, venegar</span><span class="ld"></span>$0.00</div>
    <div class="dish">Garden Roquefort</div>
    <div class="desc"><span class="t">Baby greens, arugula, beets, Roquefort P.O.V. blue cheese, caramelized pistachios, strawberries, orange vinaigrette</span><span class="ld"></span>$0.00</div>
    <div class="dish">Zucchini</div>
    <div class="desc"><span class="t">Fresh spiralized zucchini with feta, mint, almonds, lemon, P.O.V. olive oil</span><span class="ld"></span>$0.00</div>
    <div class="hd" style="margin-top:8px">Soups</div>
    <div class="dish">French Onion Soup</div>
    <div class="desc"><span class="t">Classic onion soup gratinated with gruyere cheese and crunchy eclairs</span><span class="ld"></span>$0.00</div>
    <div class="dish">Pumpkin Soup</div>
    <div class="desc"><span class="t">Homemade umpkin soup served with cream and crushed chickpeas</span><span class="ld"></span>$0.00</div>
    <div class="dish">Tomato Soup</div>
    <div class="desc"><span class="t">Tomato soup served with prosciutto gruyere cheese and crunchy eclairs</span><span class="ld"></span>$0.00</div>
    <div class="hd" style="margin-top:8px">Quiches</div>
    <div class="desc"><span class="t">available also in GF crust Larraine Mushroom Spinach Salmon tomato</span><span class="ld"></span>$0.00</div>
    <div class="hd">Phyllo Pocket</div>
    <div class="desc"><span class="t">Feta cheese served hot drizzled with honey and sesame</span><span class="ld"></span>$0.00</div>
    <div class="hd">Brioches</div>
    <div class="desc"><span class="t">Ham and cheese feta and thyme</span><span class="ld"></span>$0.00</div>
  </div>
  <div class="col r" style="top:28px">
    <div class="big" style="white-space:nowrap">Savory Eclairs</div>
    <div class="sub" style="font-size:3.2px;margin-left:2px">Side of green salad + $3.50</div>
    <div class="hd" style="margin-top:7px">Cold</div>
    <div class="dish">Tuna Salad Eclair</div>
    <div class="desc"><span class="t">Classic tuna salad with refreshing grapes and celery.</span><span class="ld"></span>$0.00</div>
    <div class="dish">Caprese Eclair</div>
    <div class="desc"><span class="t">Mozzarella cream, baby tomatoes and mozzarella pearls, topped with fresh basil and balsamic vinegar glaze</span><span class="ld"></span>$0.00</div>
    <div class="dish">Roquefort Dream Eclair (CN)</div>
    <div class="desc"><span class="t">Roquefort cream, Prosciutto, glazed pear wedges, and crushed caramelized pistachios drizzled with Balsamic fig glaze</span><span class="ld"></span>$0.00</div>
    <div class="dish">Smoked Salmon Eclair</div>
    <div class="desc"><span class="t">Whipped cream cheese with chives, smoked salmon, dill, tomatoes and onions</span><span class="ld"></span>$0.00</div>
    <div class="hd" style="margin-top:8px">Hot</div>
    <div class="dish">Shepherd's Pie Eclair</div>
    <div class="desc"><span class="t">Seasoned ground beef, topped with creamy mashed potatoes, and grated Parmesan cheese</span><span class="ld"></span>$0.00</div>
    <div class="dish">Chicken, Spinach, Artichoke Eclair</div>
    <div class="desc"><span class="t">Rich cream with spinach chicken and artichoke hearts, gratinated with parmesan, gruyere and gouda cheese</span><span class="ld"></span>$0.00</div>
    <div class="dish">Mashroom Eclair</div>
    <div class="desc"><span class="t">Creamy mashed potatoes, sauteed mushrooms, shaved Parmesan flakes, truffle oil, and chives</span><span class="ld"></span>$0.00</div>
    <div class="dish">Sweet Brie Eclair</div>
    <div class="desc"><span class="t">Melted brie, arugula, strawberry sauce and fresh strawberry halves</span><span class="ld"></span>$0.00</div>
  </div>
</section>

<!-- Petits gateaux -->
<section class="page p5">
  <div class="frame"></div>
  <div class="corner c-tl" role="img" aria-label="Corner ornament"></div><div class="corner c-tr" role="img" aria-label="Corner ornament"></div>
  <div class="corner c-bl" role="img" aria-label="Corner ornament"></div><div class="corner c-br" role="img" aria-label="Corner ornament"></div>
  <div class="col l" style="top:28px">
    <div class="hd" style="margin-top:0">Petits Gateaux</div>
    <div class="dish">Pumpkin Cheesecake</div>
    <div class="desc"><span class="t">New Fall favorite: pumpkin cheesecake served with whipped cream and drizzled with caramel</span><span class="ld"></span>$0.00</div>
    <div class="dish">Chocolate Raspberry Kiss (GF)</div>
    <div class="desc"><span class="t">Chocolate mousse with a raspberry cremeux center, on a chocolate cookie</span><span class="ld"></span>$0.00</div>
    <div class="dish">Caramel Strawberry</div>
    <div class="desc"><span class="t">Runny strawberry gelle heart on a merengue cookie enrobed with light dulcey caramel mousse</span><span class="ld"></span>$0.00</div>
    <div class="dish">NY Cheesecake Classic</div>
    <div class="desc"><span class="t">Cheesecake made of Fairdale cream cheese on a graham cracker base with a chipped cream rosette</span><span class="ld"></span>$0.00</div>
    <div class="dish">Key lime mango</div>
    <div class="desc"><span class="t">Key lime cream with the sweetness of the mango gelee with a graham cracker insert</span><span class="ld"></span>$0.00</div>
    <div class="dish">Pavlova (GF)</div>
    <div class="desc"><span class="t">Pink crispy meringue nest, filled with a light pistachio cream, pieces of fresh strawberries in red fruit gelee and topped with fluffy whipped cream and carmelized pistachios.</span><span class="ld"></span>$0.00</div>
    <div class="dish">Napoleon Millfeuille</div>
    <div class="desc"><span class="t">Indulge in the exquisite layers of delicate flaky pastry, velvety vanilla pastry cream filling, and airy chantilly that make our Millefeuille - Napoleon a true masterpiece</span><span class="ld"></span>$0.00</div>
    <div class="dish">Sunset Kiss (CN)</div>
    <div class="desc"><span class="t">Airy passion fruit panna cotta with an insert of almond biscuit and a heart of mango cremeux dipped in yellow mirror glaze and surrounded by a white and yellow chocolate piece sitting on a vanilla cookie</span><span class="ld"></span>$0.00</div>
    <div class="dish">La vie en rose (CN)</div>
    <div class="desc"><span class="t">Vanilla tart filled with almond frangipane cream and topped with an diary pineapple passionfruit mousse in the shape of a velvety rose</span><span class="ld"></span>$0.00</div>
  </div>
  <div class="col r" style="top:28px">
    <div class="hd" style="margin-top:0">Tarts</div>
    <div class="dish">Key Lime Tart</div>
    <div class="desc"><span class="t">Classic key lime tart made of lime Juice from the keys with meringue rosettes</span><span class="ld"></span>$0.00</div>
    <div class="dish">Fruit Tart</div>
    <div class="desc"><span class="t">Sweet vanilla tart filled with Vanilla cream and topped with fresh berries and seasonal fruits</span><span class="ld"></span>$0.00</div>
    <div class="big" style="margin-top:9px;line-height:.95">Vegan<br>Treats (V)</div>
    <div class="dish" style="margin-top:5px">Florentine</div>
    <div class="desc"><span class="t">Chou bun topped with vegan creamy cheese with garlic and herbs, saute spinach, 2 omelettes</span><span class="ld"></span>$15.45</div>
    <div class="dish">Avocado Toast</div>
    <div class="desc"><span class="t">Chou bun topped with vegan creamy cheese with garlic and herbs, advocado smash, sliced tomatoes, microgreens and seasam seeds served with a side of spicy honey</span><span class="ld"></span>$15.45</div>
    <div class="hd" style="margin-top:10px">Cookies</div>
    <div class="row"><span>Chocolate Chip</span><span class="ld"></span><span>$15.45</span></div>
    <div class="row"><span>Double Chocolate Chip</span><span class="ld"></span><span>$15.45</span></div>
    <div class="row"><span>Oatmeal Cinnamon</span><span class="ld"></span><span>$15.45</span></div>
    <div class="row"><span>Mini Cookies (3 pack)</span><span class="ld"></span><span>$15.45</span></div>
    <div class="hd">Verrines</div>
    <div class="row"><span>Chocolate Cake (GF)</span><span class="ld"></span><span>$15.45</span></div>
    <div class="row"><span>Lemon Berries (GF)</span><span class="ld"></span><span>$15.45</span></div>
    <div class="row"><span>Coconut Cake (GF)</span><span class="ld"></span><span>$15.45</span></div>
    <div class="hd">Muffins</div>
    <div class="row"><span>Banana Chocolate Chip</span><span class="ld"></span><span>$15.45</span></div>
    <div class="row"><span>Chocolate / Chocolate Chips</span><span class="ld"></span><span>$15.45</span></div>
    <div class="row"><span>Blueberry</span><span class="ld"></span><span>$15.45</span></div>
    <div class="row"><span>Banana Walnut (CN)</span><span class="ld"></span><span>$15.45</span></div>
  </div>
</section>

<!-- Sweet eclairs -->
<section class="page p6">
  <div class="photo" style="left:0;top:243px;width:140px;height:105px;background:linear-gradient(150deg,#f3f1ee 0%,#e9a36e 45%,#c9773e 75%,#b86a38 100%)" role="img" aria-label="Photo of a smoked salmon eclair with tomato and dill"></div>
  <div class="frame"></div>
  <div class="corner c-tl" role="img" aria-label="Corner ornament"></div><div class="corner c-tr" role="img" aria-label="Corner ornament"></div>
  <div class="corner c-bl" role="img" aria-label="Corner ornament"></div><div class="corner c-br" role="img" aria-label="Corner ornament"></div>
  <div class="big" style="position:absolute;left:77px;top:20px">Sweet Eclairs</div>
  <div class="col l" style="top:44px">
    <div class="hd">Single</div>
    <div class="dish">Chocolate Eclair</div>
    <div class="desc"><span class="t">The classic chocolate pastry fillig with chocolate glaze</span><span class="ld"></span>$0.00</div>
    <div class="dish">Vanilla Eclair</div>
    <div class="desc"><span class="t">The classic vanilla pastry filling with chocolate glaze</span><span class="ld"></span>$0.00</div>
    <div class="dish">Cofee Eclair</div>
    <div class="desc"><span class="t">Coffee creamy filling with a Caramel Coffee Glaze</span><span class="ld"></span>$0.00</div>
    <div class="dish">Tres Leches Eclair</div>
    <div class="desc"><span class="t">Tres leches cream perfumed with real rum and cinnamon, glaze in white chololate</span><span class="ld"></span>$0.00</div>
    <div class="dish">Guava Eclair</div>
    <div class="desc"><span class="t">The guava pastry filling with pink sweet glaze</span><span class="ld"></span>$0.00</div>
    <div class="dish">Strawberry Eclair</div>
    <div class="desc"><span class="t">The vanilla pastry cream and strawberry jam, dipped in red glaze</span><span class="ld"></span>$0.00</div>
    <div class="dish">Creme Brulee Eclair</div>
    <div class="desc"><span class="t">The filled with classic vanilla pastry cream and dipped in hard caramel</span><span class="ld"></span>$0.00</div>
  </div>
  <div class="note">*ALSO AVAILABLE:<br>TURKEY BACON, TURKEY HAM</div>
  <div class="legend" style="left:75px;top:252px">(CN) - CONTAINS NUTS<br>(CA) - CONTAINS ALMONDS<br>(CW) - CONTAINS WALNUTS<br>(GF) - GLUTEN FREE<br>(V) - VEGAN</div>
  <div class="col r" style="top:44px">
    <div class="hd">Double</div>
    <div class="dish">German Chocolate Eclair (CN)</div>
    <div class="desc"><span class="t">Chocolate cream filling topped with a rich sticky coconut and pecan paste dipped in hard dark chocolate with touches of gold</span><span class="ld"></span>$15.45</div>
    <div class="dish">Tiramisu Eclair</div>
    <div class="desc"><span class="t">Double eclair filled with vanilla custard cream flavored with espresso coffee cream and topped with a rich mascarpane cream with an insert of lady fingers cake</span><span class="ld"></span>$15.45</div>
    <div class="dish">Baklava Eclair (CN)</div>
    <div class="desc"><span class="t">Filled with orange pastry cream, decorated with caramelized pistachoise and pieces of fyllo dough drizzled with honey and cinnamon</span><span class="ld"></span>$15.45</div>
    <div class="dish">Tropical Passion Eclair</div>
    <div class="desc"><span class="t">Double eclair filled with mango pastry cream tonned with light passion fruit panna cotta with an insert of mango gelee</span><span class="ld"></span>$15.45</div>
    <div class="hd" style="margin-top:12px">Bread Puddings (CN)</div>
    <div class="row"><span>Mango &amp; White Chocolate (CA)</span><span class="ld"></span><span>$6.99</span></div>
    <div class="row"><span>Guava (CA)</span><span class="ld"></span><span>$6.99</span></div>
    <div class="row"><span>Brownie Walnut (contains walnuts)</span><span class="ld"></span><span>$6.99</span></div>
    <div class="row"><span>Ad a scoop fo vanilla ice-cream +</span><span class="ld"></span><span>$6.99</span></div>
    <div class="hd">Cake Pops</div>
    <div class="desc"><span class="t">Vanilla | Chocolate | Carrot Cake | V.G.F. Brownie (Contains Chickpeas)</span><span class="ld"></span>$6.99</div>
    <div class="hd">Macarons (Contain Almonds)</div>
    <div class="desc"><span class="t">White Chocolate | Dark Chocolate |</span><span class="ld"></span>$6.99</div>
    <div class="desc"><span class="t">Lemon | Apricot | Raspberry | Pistachio (contains pistachio and almond)</span><span class="ld"></span>$6.99</div>
    <div class="hd" style="margin-top:8px">Meringues</div>
    <div class="desc"><span class="t">Meringue box</span><span class="ld"></span>$6.99</div>
  </div>
</section>

</div>
</body>
</html>
```